Pinewell Fitness

I am looking for a crisp/clean website That is simple. We are looking for membership page, about us, photos, and retail sale of out clothes and accessories.

Below is our logo.

Industry/Entity Type

Retail

Number of Pages Required

4 page

Font styles to use
Sans Serif

```html
<!DOCTYPE html>
<html lang="en">
<head>
<meta charset="utf-8">
<title>Pinewell Fitness</title>
<link href="https://fonts.googleapis.com/css2?family=Michroma&family=Open+Sans:wght@400;600;700;800&display=swap" rel="stylesheet">
<style>
:root{
  --red:#d0141c;
  --red-dark:#9e0c12;
  --ink:#222;
  --dark:#1c1c1c;
  --grey:#6b6b6b;
  --light:#f3f3f3;
  --white:#fff;
}
*{box-sizing:border-box;margin:0;padding:0}
html,body{width:1200px;height:2360px;overflow:hidden}
body{font-family:"Open Sans",Arial,sans-serif;color:var(--ink);background:var(--white);position:relative}
.topbar{height:40px;background:var(--dark);color:#ccc;font-size:14px;display:flex;align-items:center;padding:0 130px}
.topbar .contact-item{display:flex;align-items:center;gap:8px;margin-right:36px}
.topbar .account{margin-left:auto;display:flex;gap:8px}
.topbar .account a{background:var(--red);color:var(--white);font-size:12px;font-weight:700;padding:5px 14px;text-decoration:none}
.header{height:125px;display:flex;align-items:stretch;justify-content:space-between;padding:0 130px;border-bottom:1px solid #e3e3e3}
.brand{display:flex;align-items:center;gap:10px;white-space:nowrap}
.brand-mark{width:18px;height:18px;background:var(--red)}
.brand-name{font-weight:800;font-size:22px;color:var(--ink);letter-spacing:1px}
.nav{display:flex;align-items:stretch}
.nav a{display:flex;align-items:center;padding:0 20px;font-size:14px;font-weight:700;color:#333;text-decoration:none;border-right:1px solid #e3e3e3;white-space:nowrap}
.nav a:last-child{border-right:none}
.nav a.home{background:var(--red);color:var(--white);flex-direction:column;justify-content:center;gap:6px;width:80px;padding:0;font-size:12px;border:none}
.hero{height:515px;background:linear-gradient(180deg,#3a3a3c 0%,#242426 60%,#3b1d1f 100%);display:flex;flex-direction:column;align-items:center;justify-content:center;color:var(--white)}
.hero-title{font-family:"Michroma",sans-serif;font-weight:400;font-size:40px;display:flex;align-items:center;gap:24px;letter-spacing:2px;text-transform:uppercase;white-space:nowrap}
.hero-title .accent{color:var(--red)}
.hero-title .rule{width:90px;height:2px;background:var(--white)}
.hero-sub{font-family:"Michroma",sans-serif;font-size:15px;letter-spacing:3px;margin-top:18px;text-transform:uppercase;white-space:nowrap}
.btn-member{margin-top:50px;display:flex;align-items:stretch;background:var(--red);color:var(--white);font-weight:700;font-size:18px;text-decoration:none}
.btn-member span{padding:14px 26px}
.btn-member i{background:var(--red-dark);width:50px;display:flex;align-items:center;justify-content:center}
.section-title{display:flex;align-items:center;justify-content:center;gap:22px;font-size:34px;font-weight:800;text-transform:uppercase;white-space:nowrap}
.section-title .rule{width:120px;height:2px;background:#444}
.section-title .accent{color:var(--red)}
.about{height:400px;background:var(--light);padding-top:36px}
.about-text{width:900px;margin:24px auto 0;text-align:center;font-size:14px;line-height:1.6;color:var(--grey)}
.services{position:relative;width:1000px;margin:34px auto 0;display:flex;justify-content:space-between}
.services::before{content:"";position:absolute;left:60px;right:60px;top:40px;height:2px;background:#333}
.service{width:240px;text-align:center;position:relative}
.service-dot{display:block;width:80px;height:80px;margin:0 auto;border-radius:50%;background:var(--red);border:16px solid var(--red);box-shadow:inset 0 0 0 40px var(--white)}
.service p{margin-top:20px;font-size:16px;font-weight:600;text-transform:uppercase}
.gallery{height:350px;padding-top:44px}
.gallery-strip{display:flex;gap:6px;width:920px;margin:34px auto 0;height:200px}
.tile{height:100%}
.tile.t1{width:190px;background:linear-gradient(135deg,#9a9a9a,#4a4a4a)}
.tile.t2{width:170px;background:#2a2a2a;color:var(--white);padding:58px 16px}
.tile.t2 h4{font-size:15px;font-weight:800}
.tile.t2 p{font-size:12px;margin-top:8px;color:#bbb;line-height:1.5}
.tile.t3{width:190px;background:linear-gradient(135deg,#c7c7c7,#6e6e6e)}
.tile.t4{width:180px;background:linear-gradient(135deg,#a8a19a,#5d5450)}
.tile.t5{width:166px;background:linear-gradient(135deg,#d8c3b0,#8c7464)}
.retail{height:610px;background:linear-gradient(180deg,#d3161d 0%,#a80f15 100%);display:flex}
.shop-col{flex:1;display:flex;flex-direction:column;align-items:center;padding-top:42px;color:var(--white)}
.shop-col+.shop-col{border-left:1px solid rgba(255,255,255,.35)}
.shop-col .section-title{font-size:30px}
.shop-col .section-title .rule{background:var(--white);width:90px}
.shop-visual{width:360px;height:300px;margin-top:26px}
.visual-clothes{background:linear-gradient(180deg,#c8765a 0%,#6e3a2f 100%)}
.visual-gear{background:linear-gradient(180deg,#cfd4d8 0%,#6c7278 100%)}
.btn-shop{margin-top:20px;background:var(--dark);color:var(--white);font-weight:800;font-size:18px;padding:14px 44px;text-decoration:none;text-transform:uppercase}
.shop-col p{margin-top:22px;width:380px;text-align:center;font-size:14px;line-height:1.6}
.footer{height:320px;background:var(--dark);color:#bbb;padding-top:34px}
.footer-cols{display:flex;justify-content:space-between;padding:0 130px}
.footer-col h5{color:var(--white);font-size:15px;font-weight:700;margin-bottom:16px;text-transform:uppercase}
.footer-col p{font-size:13px;line-height:1.6;width:240px}
.newsletter{display:flex;flex-direction:column;align-items:center}
.newsletter .field{width:300px;height:36px;background:#2c2c2c;border:1px solid #444;display:flex;align-items:center;padding:0 12px;font-size:13px;color:#888}
.reach{text-align:right}
.reach ul{list-style:none;font-size:13px;line-height:1.8}
.footer-nav{margin-top:30px;border-top:1px solid #333;padding-top:18px;display:flex;justify-content:center;font-size:13px}
.footer-nav a{color:#bbb;text-decoration:none;padding:0 18px;border-right:1px solid #555;text-transform:uppercase}
.footer-nav a:last-child{border-right:none}
.social{display:flex;justify-content:center;gap:10px;margin-top:20px}
.social span{width:26px;height:26px;border-radius:50%;background:#555}
.copyright{text-align:center;font-size:12px;margin-top:14px;color:#888}
</style>
</head>
<body>
<div class="topbar">
  <div class="contact-item">
    <svg width="14" height="14" viewBox="0 0 24 24"><path fill="#ccc" d="M6.6 10.8a15 15 0 0 0 6.6 6.6l2.2-2.2c.3-.3.7-.4 1-.2 1.1.4 2.3.6 3.6.6.6 0 1 .4 1 1V20c0 .6-.4 1-1 1A17 17 0 0 1 3 4c0-.6.4-1 1-1h3.5c.6 0 1 .4 1 1 0 1.3.2 2.5.6 3.6.1.3 0 .7-.2 1z"/></svg>
    <span>0400 555 012</span>
  </div>
  <div class="contact-item">
    <svg width="16" height="12" viewBox="0 0 24 18"><rect x="1" y="1" width="22" height="16" fill="none" stroke="#ccc" stroke-width="2"/><path d="M1 1l11 9 11-9" fill="none" stroke="#ccc" stroke-width="2"/></svg>
    <span>Contact</span>
  </div>
  <div class="account">
    <a href="#">LOGIN</a>
    <a href="#">REGISTER</a>
  </div>
</div>

<header class="header">
  <div class="brand">
    <span class="brand-mark"></span>
    <span class="brand-name">PINEWELL FITNESS</span>
  </div>
  <nav class="nav">
    <a href="#" class="home">
      <svg width="24" height="22" viewBox="0 0 26 24"><path fill="#fff" d="M13 2 1 12h3v10h7v-6h4v6h7V12h3z"/></svg>
      HOME
    </a>
    <a href="#">MEMBERSHIP</a>
    <a href="#">ABOUT US</a>
    <a href="#">PHOTO GALLERY</a>
    <a href="#">RETAIL SALE</a>
  </nav>
</header>

<section class="hero" role="img" aria-label="Photo of a woman training with a kettlebell in a dark gym">
  <h1 class="hero-title"><span class="rule"></span><span><span class="accent">Fitness</span> Made simple</span><span class="rule"></span></h1>
  <p class="hero-sub">A modern fitness program that makes getting in shape simple</p>
  <a href="#" class="btn-member"><span>BECOME A MEMBER</span><i><svg width="18" height="18" viewBox="0 0 18 18"><path d="M6 3l6 6-6 6" fill="none" stroke="#fff" stroke-width="2.5"/></svg></i></a>
</section>

<section class="about">
  <h2 class="section-title"><span class="rule"></span><span>About <span class="accent">Us</span></span><span class="rule"></span></h2>
  <p class="about-text">Pinewell Fitness keeps training simple. Small groups, friendly coaches and flexible hours help every member build strength, stamina and confidence at their own pace. Join a class, follow a plan or train with a partner, and enjoy a clean, welcoming gym that fits around your week.</p>
  <div class="services">
    <div class="service"><span class="service-dot"></span><p>Group Personal Training</p></div>
    <div class="service"><span class="service-dot"></span><p>Trek Training</p></div>
    <div class="service"><span class="service-dot"></span><p>Rotating Fitness Classes</p></div>
    <div class="service"><span class="service-dot"></span><p>Strength Training</p></div>
  </div>
</section>

<section class="gallery">
  <h2 class="section-title"><span class="rule"></span><span>Our <span class="accent">Gallery</span></span><span class="rule"></span></h2>
  <div class="gallery-strip">
    <div class="tile t1" role="img" aria-label="Photo of gym coaches standing together"></div>
    <div class="tile t2"><h4>MORNING CIRCUIT</h4><p>Fresh sessions every weekday from six.</p></div>
    <div class="tile t3" role="img" aria-label="Photo of dumbbells on a gym rack"></div>
    <div class="tile t4" role="img" aria-label="Photo of a trainer with a client holding a clipboard"></div>
    <div class="tile t5" role="img" aria-label="Photo of a smiling group of members"></div>
  </div>
</section>

<section class="retail">
  <div class="shop-col">
    <h2 class="section-title"><span class="rule"></span><span>Out Clothes</span><span class="rule"></span></h2>
    <div class="shop-visual visual-clothes" role="img" aria-label="Photo of a woman wearing training clothes"></div>
    <a href="#" class="btn-shop">Shop Now</a>
    <p>Training tees, shorts and hoodies in our own colours, made to move with you.</p>
  </div>
  <div class="shop-col">
    <h2 class="section-title"><span class="rule"></span><span>Accessories</span><span class="rule"></span></h2>
    <div class="shop-visual visual-gear" role="img" aria-label="Photo of running shoes, a water bottle and dumbbells"></div>
    <a href="#" class="btn-shop">Shop Now</a>
    <p>Bottles, bags, gloves and mats picked by our coaches for daily training.</p>
  </div>
</section>

<footer class="footer">
  <div class="footer-cols">
    <div class="footer-col">
      <h5>Pinewell Fitness</h5>
      <p>Friendly training for every level, seven days a week in the heart of town.</p>
    </div>
    <div class="footer-col newsletter">
      <h5>Sign up for newsletter</h5>
      <div class="field">Enter your email here</div>
    </div>
    <div class="footer-col reach">
      <h5>Reach us</h5>
      <ul>
        <li>(02) 5550 1847</li>
        <li>(02) 5550 1848</li>
        <li>(02) 5550 1849</li>
        <li>hello@pinewellfitness.example</li>
      </ul>
    </div>
  </div>
  <nav class="footer-nav">
    <a href="#">Home</a><a href="#">Membership</a><a href="#">About us</a><a href="#">Photo gallery</a><a href="#">Retail sale</a>
  </nav>
  <div class="social"><span></span><span></span><span></span><span></span></div>
  <p class="copyright">© 2024 Pinewell Fitness. All Rights Reserved.</p>
</footer>
</body>
</html>
```